Tech website for innovative new Aerospace company

We need a website for our Aerospace tech business. We build Test equipment for major Aerospace companies like Talvorn. I would like to have a website that differentiates us from other companies like ours such as. The links below are whats typical in our line of work. You can see the "test systems" all over these sites. This is the type of thing we build. We have an innovative new way of building these test systems that will change how the entire industry views companies like mine. The website should be visually appealing and say to the customer they should expect more than just an information and link repository.

http://www.quenlix.com/
https://www.brivo-a-tek.de/en/
https://www.tolvane.com/en/home/

You can see there is just a bunch of stuff about the company whose site the customer has come to. Now the customer has to figure out how what they need might be organized in all of this noise about News and solutions, etc. I want a website that is very customer focused - meaning "what did they come here to do"? The closest I have seen to this is from another company like ours

https://www.crestmarkusa.com/

Its still not quite what I'm looking for. Customers want to do more than just investigate potential areas of expertise I do want a part of the main page to say very clearly what it is we do, but the rest of it need to be customer focused around the task they want to do. Examples are

Learn about our modular system integration solution
Configure a test system
Get a quote or place an order
Get support
Browse products and get technical specs
Understand and lower your total cost of test
Company information
Contact us
Careers

Certain tasks like configure a system should be more prominent than others like company information

I'd like a few different types of pages designed

The product pages (don't need ecommerce) need to be hierarchical by category and allow engineers to find the product that meets their specs quickly. It should not be sales focused with too many moving marketing graphics. For example, those same pages displays the information

http://www.quenlix.com/products
https://www.brivo-a-tek.de/en/products/
https://www.tolvane.com/en/products/

The products, basic specs, price and links to manuals and data sheets should be prominently displayed and easy to compare between products

For marketing content I'd like a page design that allow for the content to be structured like a magazine page with infographics and visually appealing places to embed pictures and videos. I'll create content with info graphics that match the theme of the site. I'll need a content management system so that pages can be updated and modified to some extent without a professional website builder managing all content pushes.

For pages like support, ordering, getting a quote. It should be super easy for them to just get to where they need - whether they are looking for the phone number, contact form, downloadable order sheets etc

I am looking for a smart design concept with some dummy content in it. Once I winnow in on something that appeals to me I'll provide some more content to those I think are on the right track

Target Market(s)

Aerospace Engineers
Other Test equipment providers
Managers and leaders at Aerospace companies who are looking for a partner

Need an upscale card

Font styles to use
Sans Serif

Colors
0555a3
f37122
474747
eaeaea

Requirements
Must have
• thicker cardstock
• two tone, different color on front and back
• bevel on one corner only
• Large size company logo with logo glossy or partially glossy. Surprise me with something visually and textually interesting
Nice to have
• I personally like the type of orange listed below, but it doesn't strictly fit into our blue/grey company colors. Would be glad to see someone make it work.
• Potentially orange on back side of cardstock, grey the other, or something like that
Should not have
• Dont look anything like a standard white business card, but don't go too crazy on layout. Still has to be crisp and professional for other high level executive recipients in the Aerospace industry

```html
<!DOCTYPE html>
<html lang="en">
<head>
<meta charset="utf-8">
<title>Vantrel — Modular Test System Solutions</title>
<link rel="stylesheet" href="https://fonts.googleapis.com/css2?family=Michroma&family=Open+Sans:ital,wght@0,400;0,600;0,700;1,400;1,600&display=swap">
<style>
:root{
  --blue:#0555a3;
  --orange:#f37122;
  --ink:#474747;
  --mist:#eaeaea;
  --white:#ffffff;
  --footer:#2d2d2d;
  --footer-deep:#232323;
  --muted:#8a8a8a;
}
*{box-sizing:border-box;margin:0;padding:0}
html,body{width:1200px;height:3888px;overflow:hidden}
body{font-family:"Open Sans",Arial,sans-serif;color:var(--ink);background:var(--white);position:relative}
.display{font-family:"Michroma","Arial Black",sans-serif;text-transform:uppercase;letter-spacing:.5px;font-weight:400}
section,footer{position:relative;width:1200px}
.center{text-align:center}
.kicker{color:var(--blue);font-size:13px;font-weight:600}
.title{font-size:19px;color:#111;margin-top:12px}
.title.rule::after{content:"";display:block;width:52px;height:3px;background:var(--blue);margin:10px auto 0}
.lead{font-size:15px;font-weight:600;color:#333;line-height:1.45}
.body{font-size:11px;color:#777;line-height:1.75}
.pill{display:inline-block;border:2px solid var(--orange);border-radius:30px;padding:11px 30px;font-size:11px;font-weight:700;color:#222;text-transform:uppercase;letter-spacing:.5px;background:var(--white)}

/* hero */
.hero{height:713px;background:linear-gradient(160deg,#3a4552 0%,#1d2630 45%,#2f3b47 70%,#141b22 100%);overflow:hidden}
.hero-photo{position:absolute;inset:0;background:radial-gradient(ellipse at 80% 40%,rgba(190,200,210,.35),transparent 55%),radial-gradient(ellipse at 25% 75%,rgba(40,70,120,.55),transparent 50%),linear-gradient(180deg,rgba(0,0,0,.15),rgba(0,0,0,.45))}
.masthead{position:absolute;left:166px;top:31px;width:871px;height:104px;background:var(--white);box-shadow:0 4px 14px rgba(0,0,0,.25)}
.masthead-top{display:flex;align-items:center;height:60px;padding:0 22px;font-size:11px;color:var(--blue)}
.brand{font-family:"Michroma",sans-serif;font-size:19px;color:var(--ink);display:flex;align-items:center;gap:8px;margin-right:auto;white-space:nowrap}
.brand .dot{width:12px;height:12px;border-radius:50%;background:var(--blue)}
.info{display:flex;align-items:center;gap:6px;margin-left:22px;font-weight:600;white-space:nowrap}
.info svg{width:13px;height:13px;fill:var(--blue)}
.search{margin-left:34px;flex:none}
.masthead-nav{display:flex;align-items:center;height:44px;border-top:1px solid var(--mist);padding:0 22px}
.home-tab{width:34px;height:44px;display:flex;align-items:center;justify-content:center}
.nav a{font-size:12px;font-weight:600;color:#222;text-decoration:none;padding:0 26px;border-left:1px solid #ddd}
.nav a:first-child{border-left:none}
.social{margin-left:auto;display:flex;gap:6px}
.social span{width:18px;height:18px;border:1px solid #777;display:block}
.hero-title{position:absolute;top:282px;width:100%;font-size:32px;line-height:1.7;color:var(--white)}
.hero-btn{position:absolute;top:472px;left:533px;border:2px solid var(--white);border-radius:30px;padding:12px 28px;font-size:11px;font-weight:700;color:var(--white);letter-spacing:.5px}
.slider-nav{position:absolute;top:594px;left:440px;width:320px;display:flex;justify-content:space-between;color:var(--white);font-size:11px;font-weight:600}
.slider-nav .line{position:absolute;top:8px;left:60px;right:60px;height:1px;background:rgba(255,255,255,.6)}
.dots{position:absolute;top:659px;left:567px;display:flex;gap:8px}
.dots i{width:14px;height:14px;border-radius:50%;border:2px solid var(--white);display:block}
.dots i.on{background:var(--blue)}

/* what we do */
.what{height:427px;padding-top:57px;border-bottom:1px solid #e2e2e2}
.what .lead{margin-top:18px}
.what .body{width:720px;margin:12px auto 0;line-height:1.6}
.what-img{width:376px;height:125px;margin:38px auto 0;background:linear-gradient(90deg,#2f7a3a,#1b1b1b 50%,#3d8a44);border-radius:4px}

/* modular */
.modular{height:472px}
.frame{position:absolute;left:166px;top:60px;width:275px;height:329px;border:6px solid var(--orange)}
.frame-photo{position:absolute;left:197px;top:94px;width:275px;height:329px;background:radial-gradient(circle at 50% 55%,#6a7780,#2b3338 45%,#b9c1c7 70%,#e3e8ea)}
.modular-text{position:absolute;left:518px;top:62px;width:520px}
.modular-text .title{margin-top:10px;font-size:18px}
.modular-text .title::after{content:"";display:block;width:60px;height:3px;background:var(--blue);margin-top:10px}
.modular-text .lead{margin-top:16px}
.modular-text .body{margin-top:12px}
.modular-text .pill{margin-top:28px}

/* offerings */
.offerings{height:376px;background:#f3f3f3;padding-top:62px}
.offerings .lead{width:560px;margin:18px auto 0}
.offerings .body{width:860px;margin:10px auto 0;line-height:1.65}
.offerings .pill{margin-top:30px}

/* band */
.band{height:493px;background:linear-gradient(110deg,#9a8f83,#4d4a48 40%,#2a2f36)}
.band-photo{position:absolute;inset:0;background:radial-gradient(ellipse at 25% 40%,rgba(210,180,160,.45),transparent 45%),linear-gradient(90deg,rgba(0,0,0,.05),rgba(0,0,0,.35))}
.band-panel{position:absolute;left:601px;top:0;width:436px;height:493px;background:var(--orange);padding:56px 28px 0;color:var(--white)}
.band-notch{position:absolute;left:601px;top:493px;z-index:2}
.band-panel .kicker{color:var(--white)}
.band-panel .title{color:var(--white);font-size:15.5px;margin-top:12px;white-space:nowrap}
.band-panel .title::after{content:"";display:block;width:56px;height:3px;background:var(--white);margin-top:10px}
.band-panel .lead{color:var(--white);font-size:13px;margin-top:16px}
.band-panel .body{color:#fff;margin-top:12px}
.band-panel .pill{margin-top:22px;background:transparent;border-color:var(--white);color:var(--white)}

/* solutions */
.solutions{height:629px;padding-top:96px;border-bottom:1px solid #e2e2e2}
.solutions .title{width:900px;margin:10px auto 0;font-size:15.5px;line-height:1.75}
.cards{display:flex;justify-content:center;gap:20px;margin-top:36px}
.card{width:260px;text-align:center}
.card-img{height:163px}
.card small{display:block;margin-top:30px;font-size:9px;color:#999;letter-spacing:1px;font-weight:600}
.card h3{font-size:12px;font-weight:700;color:#111;margin-top:8px}
.card p{font-size:10.5px;color:#888;line-height:1.6;margin-top:6px;padding:0 14px}
.card .bar{width:1px;height:14px;background:#777;margin:6px auto 0}
.card a{display:inline-block;margin-top:4px;font-size:10px;font-weight:700;color:#222;text-decoration:underline}

/* testimonial */
.testimonial{height:410px;padding-top:52px}
.testimonial .title::after{content:"";display:block;width:52px;height:3px;background:var(--blue);margin:10px auto 0}
.quote{display:block;margin:20px auto 0;width:44px}
.testimonial blockquote{width:740px;margin:12px auto 0;font-size:14px;font-style:italic;font-weight:600;color:#333;line-height:1.6}
.testimonial .name{margin-top:20px;font-size:17px;color:#222}
.testimonial .date{font-size:11px;color:#777;margin-top:2px}
.arrows{display:flex;justify-content:center;gap:6px;margin-top:10px}
.arrows span{width:18px;height:18px;border-radius:50%;background:#bbb;display:flex;align-items:center;justify-content:center}
.arrows span.on{background:#222}

/* footer */
.footer{height:368px;background:var(--footer);border-top:5px solid var(--blue);color:#bbb}
.footer-top{position:absolute;left:166px;top:36px;width:871px;display:flex;align-items:center;justify-content:space-between;padding-bottom:26px;border-bottom:1px solid #444}
.footer .brand{color:#ddd;font-size:19px;margin:0}
.footer .social{margin-left:0}
.footer .social span{border-color:#ccc;background:#fff}
.cols{position:absolute;left:166px;top:140px;width:871px;display:flex}
.col h4{font-size:11px;color:#fff;font-weight:700;margin-bottom:16px}
.col ul{padding:0}
.col li{list-style:none;font-size:10.5px;color:#999;margin-bottom:12px;display:flex;gap:8px;align-items:flex-start;line-height:1.5}
.col svg{width:11px;height:11px;fill:#999;flex:none;margin-top:3px}
.col p{font-size:10.5px;color:#999;line-height:1.7}
.footer-bar{position:absolute;left:0;bottom:0;width:1200px;height:39px;background:var(--footer-deep);display:flex;align-items:center;padding:0 166px;font-size:10.5px;color:#aaa}
.footer-bar a{color:#aaa;text-decoration:none;margin-right:46px}
.footer-bar a.right{margin:0 0 0 auto}
</style>
</head>
<body>

<section class="hero">
  <div class="hero-photo" role="img" aria-label="Technicians loading equipment beside an aircraft at night"></div>

  <header class="masthead">
    <div class="masthead-top">
      <div class="brand"><span class="dot"></span>VANTREL</div>
      <div class="info"><svg viewBox="0 0 24 24"><path d="M6.6 10.8a15 15 0 0 0 6.6 6.6l2.2-2.2c.3-.3.7-.4 1-.2 1.1.4 2.3.6 3.6.6.6 0 1 .4 1 1V20c0 .6-.4 1-1 1A17 17 0 0 1 3 4c0-.6.4-1 1-1h3.5c.6 0 1 .4 1 1 0 1.2.2 2.4.6 3.6.1.3 0 .7-.2 1z"/></svg>+1234567891</div>
      <div class="info"><svg viewBox="0 0 24 24"><path d="M12 2a7 7 0 0 0-7 7c0 5 7 13 7 13s7-8 7-13a7 7 0 0 0-7-7zm0 9.5A2.5 2.5 0 1 1 12 6a2.5 2.5 0 0 1 0 5.5z"/></svg>Lorem Ipsum is dummy text here,</div>
      <div class="info"><svg viewBox="0 0 24 24"><path d="M2 5h20v14H2zm2 2v.5l8 5 8-5V7z"/></svg>hello@vantrel.us</div>
      <svg class="search" width="16" height="16" viewBox="0 0 24 24"><circle cx="10" cy="10" r="7" fill="none" stroke="#0555a3" stroke-width="3"/><path d="M15 15l6 6" stroke="#0555a3" stroke-width="3"/></svg>
    </div>
    <nav class="masthead-nav">
      <div class="home-tab"><svg width="16" height="15" viewBox="0 0 24 22"><path d="M12 1L1 11h3v10h6v-6h4v6h6V11h3z" fill="#0555a3"/></svg></div>
      <div class="nav" style="margin-left:14px"><a>Home</a><a>Products</a><a>Solutions</a><a>Company</a><a>Contact</a></div>
      <div class="social"><span></span><span></span><span></span><span></span></div>
    </nav>
  </header>

  <h1 class="hero-title display center">Reinventing Test<br>With Modular System Solutions</h1>
  <div class="hero-btn">GET SUPPORT</div>
  <div class="slider-nav"><span>PREV</span><span class="line"></span><span>NEXT</span></div>
  <div class="dots"><i></i><i class="on"></i><i></i></div>
</section>

<section class="what center">
  <div class="kicker">Vantrel is ready to help</div>
  <h2 class="title display">What We Do</h2>
  <p class="lead">We build Test equipment for major Aerospace<br>companies like Talvorn</p>
  <p class="body">Vantrel has partnered with Norvane Instruments to develop a modular system architecture that allows for rapid design and integration of systems of any size. For any portion of a system that is truly universal between multiple product lines, the design becomes configuration.</p>
  <div class="what-img" role="img" aria-label="Circuit boards and a modular test instrument"></div>
</section>

<section class="modular">
  <div class="frame"></div>
  <div class="frame-photo" role="img" aria-label="Close view of a jet engine fan"></div>
  <div class="modular-text">
    <div class="kicker">Vantrel is ready to help</div>
    <h2 class="title display">Modular System Solutions</h2>
    <p class="lead">Our innovative new system level platform can dramatically improve your test schedule while controlling project risk and equipment budgets</p>
    <p class="body">Vantrel has partnered with Norvane Instruments to develop a modular system architecture that allows for rapid design and integration of systems of any size. For any portion of a system that is truly universal between multiple product lines, the design becomes configuration and the integration becomes assembly – all with off the shelf instrumentation and cables out to the pin. For anything that truly must be custom for a program, those components are compartmentalized and isolated, so the design of those elements does not affect the common core.</p>
    <span class="pill">Get a Quote</span>
  </div>
</section>

<section class="offerings center">
  <div class="kicker">Vantrel is ready to help</div>
  <h2 class="title display">Vantrel Offerings</h2>
  <p class="lead">From hardware and software configuration services, to complete standardization solutions, we can help you accelerate your test program</p>
  <p class="body">Vantrel has partnered with Norvane Instruments to develop a modular system architecture that allows for rapid design and integration of systems of any size. For any portion of a system that is truly universal between multiple product lines, the design becomes configuration and the integration becomes assembly – all with off the shelf instrumentation and cables out to the pin. For anything that truly must be custom for a program...</p>
  <span class="pill">Learn More</span>
</section>

<section class="band">
  <div class="band-photo" role="img" aria-label="Engineer explaining a test setup to two young colleagues"></div>
  <div class="band-panel">
    <div class="kicker">Vantrel is ready to help</div>
    <h2 class="title display">Modular System Solutions</h2>
    <p class="lead">Proven best in class solutions Prototyping, Verification &amp; Validation, Production and Aftermarket Testing for Aerospace LRU Programs</p>
    <p class="body">Vantrel has partnered with Norvane Instruments to develop a modular system architecture that allows for rapid design and integration of systems of any size. For any portion of a system that is truly universal between multiple product lines, the design becomes configuration and the integration becomes assembly – all with off the shelf instrumentation and cables out to the pin. For anything that truly must be custom for a program, those components are compartmentalized and isolated, so the design of those elements does not affect the common core.</p>
    <span class="pill">Learn More</span>
  </div>
  <svg class="band-notch" width="436" height="12" viewBox="0 0 436 12"><path d="M0 0h436l-12 12H12z" fill="#d85f15"/></svg>
</section>

<section class="solutions center">
  <div class="kicker">SOLUTIONS</div>
  <h2 class="title display">We have an innovative new way of building these test systems that will change how the entire industry views companies like mine.</h2>
  <div class="cards">
    <article class="card">
      <div class="card-img" role="img" aria-label="Technician servicing an engine in a hangar" style="background:linear-gradient(135deg,#3b6fa8,#8a6d4a 55%,#2f3a45)"></div>
      <small>LOREM IPSUM IS DUMMY TEXT</small>
      <h3>AUTOMATED TEST SOLUTIONS</h3>
      <p>We have an innovative new way of building these test systems that will change how the entire industry views companies like mine that allows</p>
      <div class="bar"></div><a>Learn More</a>
    </article>
    <article class="card">
      <div class="card-img" role="img" aria-label="Jet engine on a maintenance stand" style="background:radial-gradient(circle at 55% 50%,#55606a,#2a2f33 50%,#8f7e6c)"></div>
      <small>LOREM IPSUM IS DUMMY TEXT</small>
      <h3>AUTOMATED TEST SOLUTIONS</h3>
      <p>We have an innovative new way of building these test systems that will change how the entire industry views companies like mine that allows</p>
      <div class="bar"></div><a>Learn More</a>
    </article>
    <article class="card">
      <div class="card-img" role="img" aria-label="Aircraft on the apron with ground crew" style="background:linear-gradient(160deg,#c9ccd0,#9aa1a8 50%,#5a6168)"></div>
      <small>LOREM IPSUM IS DUMMY TEXT</small>
      <h3>AUTOMATED TEST SOLUTIONS</h3>
      <p>We have an innovative new way of building these test systems that will change how the entire industry views companies like mine that allows</p>
      <div class="bar"></div><a>Learn More</a>
    </article>
  </div>
</section>

<section class="testimonial center">
  <div class="kicker">Vantrel is ready to help</div>
  <h2 class="title display">What Our Client Say</h2>
  <svg class="quote" width="44" height="36" viewBox="0 0 44 36"><path d="M0 36V20C0 8 6 2 17 0l2 5c-6 2-9 6-9 11h8v20zm25 0V20c0-12 6-18 17-20l2 5c-6 2-9 6-9 11h8v20z" fill="#f37122"/></svg>
  <blockquote>Lorem Ipsum is simply dummy text of the printing and typesetting industry. Lorem Ipsum has been the industry's standard dummy text ever since the 1500s, when an unknown printer took a galley of type and scrambled it to make a type specimen book.</blockquote>
  <div class="name">Marlo Teskin</div>
  <div class="date">Date : 21 June 018</div>
  <div class="arrows">
    <span><svg width="8" height="8" viewBox="0 0 8 8"><path d="M6 0L2 4l4 4" fill="none" stroke="#fff" stroke-width="1.6"/></svg></span>
    <span class="on"><svg width="8" height="8" viewBox="0 0 8 8"><path d="M2 0l4 4-4 4" fill="none" stroke="#fff" stroke-width="1.6"/></svg></span>
  </div>
</section>

<footer class="footer">
  <div class="footer-top">
    <div class="brand">VANTREL</div>
    <div class="social"><span></span><span></span><span></span><span></span></div>
  </div>
  <div class="cols">
    <div class="col" style="width:264px">
      <h4>CONTACT US</h4>
      <ul>
        <li><svg viewBox="0 0 24 24"><path d="M6.6 10.8a15 15 0 0 0 6.6 6.6l2.2-2.2c.3-.3.7-.4 1-.2 1.1.4 2.3.6 3.6.6.6 0 1 .4 1 1V20c0 .6-.4 1-1 1A17 17 0 0 1 3 4c0-.6.4-1 1-1h3.5c.6 0 1 .4 1 1 0 1.2.2 2.4.6 3.6.1.3 0 .7-.2 1z"/></svg>+1234567891</li>
        <li><svg viewBox="0 0 24 24"><path d="M12 2a7 7 0 0 0-7 7c0 5 7 13 7 13s7-8 7-13a7 7 0 0 0-7-7z"/></svg>Lorem Ipsum is dummy text<br>industry</li>
        <li><svg viewBox="0 0 24 24"><path d="M2 5h20v14H2zm2 2v.5l8 5 8-5V7z"/></svg>hello@vantrel.us</li>
      </ul>
    </div>
    <div class="col" style="width:187px">
      <h4>QUICK LINKS</h4>
      <ul>
        <li>→&nbsp; About Us</li>
        <li>→&nbsp; Site Map</li>
        <li>→&nbsp; Help</li>
        <li>→&nbsp; Contact</li>
      </ul>
    </div>
    <div class="col" style="width:295px">
      <h4>INFORMATION</h4>
      <p>Lorem Ipsum is simply dummy text<br>of the printing and typesetting<br>industry text.</p>
      <p style="color:#ddd;margin-top:6px">Read More →</p>
    </div>
    <div class="col">
      <p style="margin-top:28px">© Copyright 2018 Vantrel.<br>All Rights Reserved.</p>
    </div>
  </div>
  <div class="footer-bar">
    <a>Home</a><a>Product</a><a>Solutions</a><a>Company</a><a>Contact</a><a class="right">Privacy Policy</a>
  </div>
</footer>

</body>
</html>
```